Webdesign Chiropraktik
Zielgruppe
Amerikanische Chiropraktik
Aufgabenstellung
keine direkten vorgaben...Wir sind ein junges Team und brauchen eine moderne ansprechende Webseite...

```html
<!DOCTYPE html>
<html lang="de">
<head>
<meta charset="utf-8">
<title>Vitalwerk Chiropraktik</title>
<link href="https://fonts.googleapis.com/css2?family=Libre+Bodoni:wght@600;700&family=Source+Sans+3:wght@400;600;700&display=swap" rel="stylesheet">
<style>
:root{
  --ink:#161a2b;
  --light:#edf1f5;
  --peach:#f1e2d8;
  --green:#b5dca4;
  --green-soft:#cde8c6;
  --card:#e9eef4;
  --star:#f5b82e;
  --text:#2a2e3c;
}
*{margin:0;padding:0;box-sizing:border-box}
html,body{width:1200px;height:3900px;overflow:hidden}
body{position:relative;background:var(--light);font-family:"Source Sans 3",Arial,sans-serif;color:var(--text)}
.abs{position:absolute}
.serif{font-family:"Libre Bodoni",Georgia,serif;font-weight:700;color:var(--ink);letter-spacing:-0.5px}
.eyebrow{font-size:12px;letter-spacing:3px;text-transform:uppercase}
.photo{position:absolute}
/* hero */
.hero-panel{left:696px;top:8px;width:497px;height:717px;background:linear-gradient(160deg,#f2e4da,#eedcd0)}
.brand{left:108px;top:68px;font-size:20px;font-weight:700;color:var(--ink)}
.nav a{position:absolute;top:40px;font-size:12px;color:var(--ink);text-decoration:none}
.phone{left:1006px;top:26px;width:166px;height:39px;background:var(--green);color:var(--ink);font-weight:700;font-size:15px;letter-spacing:1px;display:flex;align-items:center;justify-content:center;box-shadow:0 10px 20px rgba(0,0,0,.08)}
.hero-title{left:112px;top:244px;font-size:58px;line-height:1.12}
.hero-text{left:112px;top:394px;font-size:16px;line-height:26px;color:var(--ink)}
.btn-dark{background:var(--ink);color:#fff;font-weight:700;font-size:13px;letter-spacing:.8px;display:flex;align-items:center;justify-content:center}
.icon-box{left:842px;top:208px;width:58px;height:57px;background:#fff;display:flex;align-items:center;justify-content:center}
.review{left:619px;top:438px;width:308px;height:97px;background:#fff;padding:14px 20px;box-shadow:0 10px 25px rgba(0,0,0,.06)}
.review .who{display:flex;align-items:center;gap:10px;font-family:"Libre Bodoni",Georgia,serif;font-size:14px;color:var(--ink)}
.avatar{width:26px;height:26px;border-radius:50%;background:#b7a596;display:inline-block}
.stars{color:var(--star);font-size:14px;letter-spacing:2px;margin-left:auto}
.review p{font-size:12px;line-height:18px;margin-top:8px}
/* dark */
.dark{left:0;top:733px;width:1200px;height:1645px;background:var(--ink)}
.light-on-dark{color:#fff}
.step{position:absolute;top:1016px;width:311px;height:283px;padding:38px 0 0 84px}
.step h3{font-family:"Libre Bodoni",Georgia,serif;font-size:18px;color:var(--ink);margin-top:52px}
.step p{font-size:13px;line-height:26.5px;margin-top:8px;width:200px;color:var(--ink)}
.step .arrow{position:absolute;left:38px;top:126px}
.quote{left:579px;top:1752px;width:450px;height:252px;background:#fff;padding:30px 32px}
.quote p{font-size:19px;font-weight:600;line-height:27px;color:var(--ink)}
.quote .by{display:flex;align-items:center;gap:14px;margin-top:20px;font-size:15px;color:var(--ink)}
.quote .avatar{width:38px;height:38px;background:#1f2430}
.dots{top:2057px;height:3px}
/* cta */
.cta{left:112px;top:2218px;width:984px;height:238px;background:linear-gradient(100deg,#a9d69a 0%,#bfe2b3 40%,#d3ecce 100%);box-shadow:0 30px 40px -20px rgba(0,0,0,.12)}
.cta p{position:absolute;left:84px;top:112px;width:600px;font-size:16px;line-height:26.5px;color:var(--ink)}
/* info */
.info p{font-size:15.5px;line-height:26.6px;color:var(--ink);width:650px;margin-bottom:26.6px}
.circle-btn{position:absolute;top:3210px;width:40px;height:40px}
</style>
</head>
<body>

<!-- Hero -->
<div class="abs hero-panel"></div>
<svg class="abs" style="left:696px;top:8px" width="497" height="717" viewBox="0 0 497 717"><path d="M250 0 C 300 150 420 220 497 250 V0Z" fill="#f4e9e1" opacity=".7"/><path d="M0 600 C 120 520 260 540 330 717 H0Z" fill="#f4e9e1" opacity=".7"/></svg>
<div class="abs brand">Vitalwerk</div>
<nav class="nav">
  <a style="left:245px">Ablauf</a>
  <a style="left:315px">Feadback</a>
  <a style="left:403px">Bilder</a>
  <a style="left:471px">Contact Us</a>
</nav>
<div class="abs phone">08140 5527310</div>

<div class="abs eyebrow" style="left:112px;top:213px;color:var(--ink)">Chiropraktik</div>
<h1 class="abs serif hero-title">Herzlich<br>Willkommen.</h1>
<p class="abs hero-text">Hier beginnt Ihre Reise mit der<br>amerikanischen Chiropraktik</p>
<div class="abs btn-dark" style="left:112px;top:512px;width:194px;height:39px">TERMIN VEREINBAREN</div>

<div class="photo" role="img" aria-label="Nahaufnahme einer Behandlung mit Justierinstrument am Rücken" style="left:619px;top:173px;width:196px;height:240px;background:linear-gradient(160deg,#2b2422,#a77e6c 60%,#e6c2b2)"></div>
<div class="abs icon-box"><svg width="26" height="20" viewBox="0 0 26 20" fill="none" stroke="#161a2b" stroke-width="2"><path d="M2 3h22v6H2z M5 9v9 M21 9v9 M8 3v6 M13 3v6 M18 3v6"/></svg></div>
<div class="photo" role="img" aria-label="Chiropraktiker behandelt eine Patientin auf der Liege" style="left:842px;top:293px;width:252px;height:307px;background:linear-gradient(170deg,#ede5db,#c9b3a3 45%,#1e2026 75%,#3a3f50)"></div>
<div class="abs review">
  <div class="who"><span class="avatar"></span>Lena Hofbauer<span class="stars">★★★★★</span></div>
  <p>Es ist unglaublich was Tobias Ranftl &nbsp;bei<br>meinem Körper bewirken konnte.</p>
</div>

<!-- Dark section -->
<div class="abs dark"></div>
<div class="abs eyebrow light-on-dark" style="left:196px;top:874px">So arbeiten wir</div>
<h2 class="abs serif light-on-dark" style="left:196px;top:906px;font-size:44px;color:#fff">Ablauf</h2>

<div class="step" style="left:112px;background:linear-gradient(135deg,#a9d598,#bfe1b1)">
  <svg width="30" height="30" viewBox="0 0 30 30" fill="none" stroke="#161a2b" stroke-width="2"><path d="M3 3h24v18H15l-6 6v-6H3z"/><circle cx="11" cy="10" r="1" fill="#161a2b"/><circle cx="19" cy="10" r="1" fill="#161a2b"/><path d="M10 14c3 3 7 3 10 0"/></svg>
  <svg class="arrow" width="20" height="12" viewBox="0 0 20 12" fill="none" stroke="#161a2b" stroke-width="1.6"><path d="M0 6h18M13 1l5 5-5 5"/></svg>
  <h3>Anamnesegespräch</h3>
  <p>Der Ersttermin umfasst ein ausführliches Anamnesegespräch, eine…</p>
</div>
<div class="step" style="left:449px;background:linear-gradient(135deg,#f0f3f7,#e4eaf2)">
  <svg width="30" height="30" viewBox="0 0 30 30" fill="none" stroke="#161a2b" stroke-width="2"><rect x="3" y="5" width="24" height="22" rx="2"/><path d="M3 12h24M9 2v6M21 2v6"/></svg>
  <svg class="arrow" width="20" height="12" viewBox="0 0 20 12" fill="none" stroke="#161a2b" stroke-width="1.6"><path d="M0 6h18M13 1l5 5-5 5"/></svg>
  <h3>Behandlungsplan</h3>
  <p>Nach dieser Sitzung wird ein individueller Behandlungsplan für Sie erstellt.</p>
</div>
<div class="step" style="left:786px;background:linear-gradient(135deg,#e3ebf4,#eef2f6)">
  <svg width="36" height="30" viewBox="0 0 36 30" fill="none" stroke="#161a2b" stroke-width="2"><path d="M2 15C8 5 28 5 34 15 28 25 8 25 2 15z"/><circle cx="18" cy="15" r="6"/><circle cx="18" cy="15" r="2.5"/></svg>
  <svg class="arrow" width="20" height="12" viewBox="0 0 20 12" fill="none" stroke="#161a2b" stroke-width="1.6"><path d="M0 6h18M13 1l5 5-5 5"/></svg>
  <h3>Untersuchung</h3>
  <p>In der körperlichen Untersuchung wird der ganze Körper in Statik und aktiver…</p>
</div>

<div class="abs eyebrow light-on-dark" style="left:196px;top:1438px">Kundenmeinungen</div>
<h2 class="abs serif" style="left:196px;top:1468px;font-size:44px;line-height:54px;color:#fff">Unsere Kunden<br>über uns</h2>
<div class="photo" role="img" aria-label="Praxisraum, Chiropraktiker justiert die Schulter einer Patientin" style="left:112px;top:1631px;width:984px;height:479px;background:linear-gradient(115deg,#c9bfb5 0%,#6f5c52 25%,#2a2528 45%,#d8cdc3 70%,#9fb5b4 100%)"></div>
<div class="abs quote">
  <p>1A, besser geht's nicht! Tobias und sein Team sind wirklich "outstanding". Tobias ist ein extrem guter und kompetenter Chiropraktiker. Bin jetzt seit einiger Zeit bei ihm und er renkt mich regelmäßig wieder…</p>
  <div class="by"><span class="avatar"></span>Jonas Wallner<span class="stars">★★★★★</span></div>
</div>
<div class="abs dots" style="left:517px;width:48px;background:#161a2b"></div>
<div class="abs dots" style="left:575px;width:48px;background:rgba(22,26,43,.35)"></div>
<div class="abs dots" style="left:633px;width:48px;background:rgba(22,26,43,.35)"></div>

<!-- CTA -->
<div class="abs cta">
  <h2 class="abs serif" style="left:84px;top:50px;font-size:44px">Terminanfrage</h2>
  <p>Der Ersttermin umfasst ein ausführliches Anamnesegespräch, eine körperliche Untersuchung und die anschließende Behandlung (Justierung). Nach dieser Sitzung wird ein individueller Behandlungsplan für Sie erstellt.</p>
  <div class="abs btn-dark" style="left:766px;top:106px;width:141px;height:38px;font-family:'Libre Bodoni',Georgia,serif;font-size:12px;letter-spacing:1.2px">CONTACT US</div>
</div>

<!-- Info -->
<div class="abs eyebrow" style="left:199px;top:2583px;font-size:11.5px;color:var(--ink)">Amerikanische Chiropraktik nun auch in Haldenau!</div>
<h2 class="abs serif" style="left:196px;top:2612px;font-size:44px">Chiropraktik in Haldenau</h2>
<div class="abs info" style="left:196px;top:2695px">
  <p>Die Chiropraktik beschäftigt sich primär mit den Störungen des Nervensystems im Körper. Gibt es in unserem Hauptorgan (Gehirn) einen Fehler/Schwäche kann sich das in unserem Körper spiegeln! Meistens reagiert der Körper mit einer lokalen Verspannung eines Muskels.</p>
  <p>Daraus kann eine Einschränkung der Gelenkbeweglichkeit resultieren. Der Chiropraktiker muss also mittels neurologischen Tests herausfinden, wo sich der Fehler im Gehirn befindet. Durch gezielte Justierungen an der Wirbelsäule und an peripheren Gelenken kann der Chiropraktiker das Gehirn positiv beeinflussen. Je weniger Fehler im Gehirn, desto besser die Funktion des Körpers -&gt; WENIGER Symptome!</p>
  <p>Wird das Gehirn, wie bei allen Aktivitäten, regelmäßig positiv stimuliert, gibt es sowohl im Gehirn als auch im Körper positive Veränderungen. Heilung ist also ein Prozess und kein Event</p>
</div>

<h2 class="abs serif" style="left:196px;top:3148px;font-size:44px;line-height:54px">Überzeugen<br>Sie sich selber</h2>
<svg class="circle-btn" style="left:953px" viewBox="0 0 40 40" fill="none" stroke="#161a2b" stroke-width="1.5"><circle cx="20" cy="20" r="19"/><path d="M29 20H12M17 15l-5 5 5 5"/></svg>
<svg class="abs" style="left:1013px;top:3228px" width="22" height="4" viewBox="0 0 22 4"><circle cx="2" cy="2" r="2" fill="#161a2b"/><circle cx="11" cy="2" r="1.2" fill="#161a2b"/><circle cx="19" cy="2" r="1.2" fill="#161a2b"/></svg>
<svg class="circle-btn" style="left:1055px" viewBox="0 0 40 40" fill="none" stroke="#161a2b" stroke-width="1.5"><circle cx="20" cy="20" r="19"/><path d="M11 20h17M23 15l5 5-5 5"/></svg>

<div class="photo" role="img" aria-label="Heller Behandlungsraum mit Liege, Tisch und Wandtafeln" style="left:112px;top:3297px;width:816px;height:500px;background:linear-gradient(180deg,#eceae6 0%,#e4e1dc 55%,#c39a74 80%,#a9805e 100%)"></div>
<div class="photo" role="img" aria-label="Chiropraktiker im schwarzen Shirt vor Wandbild" style="left:954px;top:3297px;width:246px;height:500px;background:linear-gradient(160deg,#a9c0c3,#d7dad3 35%,#1c1d22 60%,#121316)"></div>

</body>
</html>
```